Double-Gate-Fold Mailer (8-panels)

I have an 8-panel brochure/mailer that I need designed. We're looking for something very classy and professional-looking (both in the fonts and the imagery chosen), as this is for a medical educational event for doctors - and our members are very discerning.

We're open to any design idea that fits within the parameters given below, but if it helps, our primary color is PMS 295 (Hex #002e5a) and we often use PMS 452 (Hex #aaa77e) as a contrasting color.

Images using the NYC skyline or major landmarks are fine, as this will be held in NYC again this year. I have attached photos of the venues that could be used as pop-out images, faded background images or for other inspiration. (I do not have higher-resolution versions of any of the venue photos.)

More info about this event can be found here: http://brelvanguild.org/2017annualmtg/

Important Notes:

- This year's mailer needs to be 20.75" x 8.75” (flat), which will be folded down to 5.19" x 8.75" ultimately.

- I will provide final text for designer, but I have attached last year's mailer so that you can use the content from this as placeholder text. Latin text is also fine - just looking for the design right now.

- *** This year's mailer WILL NOT HAVE a registration form, so please don't include the registration form portion in your design. *** We have, however, added an extra session this year (the day before), so the extra space could be used to promote this new 4-hour event.

- In case it matters to your design, the two events will be in two different locations.

- Final deliverable must include raw files, including main project file (either .ai, .idml, or psd format) and fonts, images, etc.
Updates

Project Deadline Extended Reason: While there are a couple that are interesting and some that are close to our in-house style and tone, I haven't yet seen an outstanding entry (one that followed the directions) yet, especially with respect to subtle/minimal imagery. I would like to give it a few more days. Added Wednesday, July 19, 2017

Target Market(s)

Physicians, nurses, technologists (Please do not use stock images of physicians, nurses, etc. This is a direct-mail brochure; they will know it is for them.)

Industry/Entity Type

Education

Font styles to use
Serif
Sans Serif

Colors

Designer to choose colors to be used in the design.

Requirements
Must have
• Must have room for all content to fit. Last year's brochure is attached as an example of the amount of content there will be. I have attached the five (5) logos that will (eventually) need to be on the brochure. They can be added later either in full color or monotone.
• This year doesn't have a theme like last year. The title of the event is simply: "The 89th Annual Scientific Session & Inaugural PQR Quillbox Challenge"
Nice to have
• Nice to have a design that somehow coordinates with our logos, which, as you can see, range in color from dark blue to light blue, but this isn't necessary, as our logos can all be monotone if necessary. It would be nice if the designer could keep the horizontal-style of the art, similar to last year's, but it's not a requirement.
Should not have
• Images should be subtle, faded or pushed to the background. Please don't include stock images of people, physicians working, medical equipment, etc. (This is a highly specialized field of medicine, and generic stock images look very strange and, at best, are a misrepresentation of these doctors.) Art should not be to "cartoon-y" either or have too many distracting images.

```html
<!DOCTYPE html>
<html lang="en">
<head>
<meta charset="utf-8">
<title>Cardiology for the Ages – Gate-Fold Mailer</title>
<link rel="stylesheet" href="https://fonts.googleapis.com/css2?family=Roboto:wght@300;400;500&family=Roboto+Condensed:wght@500;700&family=Lato:wght@400;700&display=swap">
<style>
:root{
  --bg:#e9e7e2;
  --paper:#ffffff;
  --navy:#0d3c6e;
  --blue:#1f6aa8;
  --band:#1c64a0;
  --ink:#3b3f45;
  --muted:#6d737a;
  --rule:#c9ced4;
}
*{box-sizing:border-box;margin:0;padding:0}
html,body{width:1200px;height:1200px;overflow:hidden;background:var(--bg)}
body{font-family:"Lato",sans-serif;color:var(--ink)}
.mailer{position:absolute;left:20px;top:355px;width:1160px;height:490px;display:flex;box-shadow:0 6px 18px rgba(0,0,0,.18)}
.panel{position:relative;width:290px;height:490px;background:var(--paper);overflow:hidden;border-bottom:4px solid var(--band)}
.panel + .panel{border-left:1px solid #eceef0}

/* roster panel */
.roster{padding:18px 12px 0 12px}
.org{margin-bottom:12px}
.org-title{font-family:"Roboto",sans-serif;font-weight:400;font-size:9.5px;color:var(--blue);display:flex;align-items:center;gap:6px;margin-bottom:5px}
.org-title::after{content:"";flex:1;height:1px;background:var(--rule)}
.group{font-size:5.2px;font-weight:700;color:var(--blue);letter-spacing:.2px;margin:4px 0 2px}
.cols{display:grid;grid-template-columns:1fr 1fr;column-gap:10px}
.officer{font-size:5px;line-height:1.3;margin-bottom:3px}
.officer b{text-transform:uppercase;color:#23282e}
.names{font-size:4.8px;line-height:1.55;color:var(--muted)}

/* mailing panel */
.return{position:absolute;left:76px;bottom:22px;width:150px;height:100px}
.vline{position:absolute;bottom:0;transform-origin:left bottom;transform:rotate(-90deg);white-space:nowrap;font-size:5px;line-height:1.35;color:var(--ink)}
.vline b{color:#23282e}
.seal{position:absolute;left:22px;bottom:30px;width:30px;height:30px;border:1.5px solid var(--muted);border-radius:50%}
.map{position:absolute;right:20px;bottom:24px;width:105px;height:80px;background:linear-gradient(135deg,#2a6478 0%,#5fb8cf 45%,#2b5f74 100%)}

/* cover panel */
.cover-photo{position:absolute;left:0;top:0;width:290px;height:345px;background:
  linear-gradient(to bottom,rgba(255,255,255,0) 55%,#fff 100%),
  linear-gradient(to bottom,#bfe0ea 0%,#d9dccf 30%,#9aa3a6 60%,#8a8e8c 80%)}
.cover-title{position:absolute;left:0;right:0;top:262px;text-align:center}
.cover-title .l1{font-family:"Roboto",sans-serif;font-size:17px;color:var(--blue);font-weight:400}
.cover-title .l2{font-family:"Roboto",sans-serif;font-size:19px;color:#2a3038;font-weight:300;margin-top:2px}
.cover-title .l3{font-family:"Roboto Condensed",sans-serif;font-size:18px;color:var(--navy);font-weight:700;margin-top:4px;letter-spacing:.3px}
.date-band{position:absolute;left:0;top:345px;width:290px;height:62px;background:var(--band);color:#fff;padding:10px 0 0 62px}
.date-band .row{display:flex;align-items:flex-start;gap:7px;position:relative}
.date-band svg{position:absolute;left:-20px;top:0}
.date-band .when{font-size:8.5px;font-weight:700;line-height:1.25}
.date-band .when span{font-weight:400}
.date-band .where{font-size:6.5px;line-height:1.35;margin-top:6px}
.date-band .where b{font-weight:700}
.partners{position:absolute;left:22px;right:14px;top:418px;display:grid;grid-template-columns:1fr 1fr;row-gap:12px;column-gap:8px}
.partner{display:flex;gap:5px;align-items:center;font-size:4.9px;line-height:1.3;color:var(--muted)}
.partner i{flex:none;width:14px;height:14px;border-radius:50%;border:1.2px solid var(--navy)}

/* program panel */
.program{padding:20px 12px 0 14px}
.h{font-family:"Roboto",sans-serif;font-size:7.5px;color:var(--blue);margin:0 0 3px}
.program p{font-size:4.8px;line-height:1.5;text-align:justify;margin-bottom:8px}
.program ul{list-style:none;margin-bottom:8px}
.program li{font-size:4.7px;line-height:1.45;padding-left:6px;position:relative;margin-bottom:2px}
.program li::before{content:"";position:absolute;left:0;top:2.4px;width:2px;height:2px;border-radius:50%;background:var(--blue)}
</style>
</head>
<body>
<main class="mailer">

  <!-- Panel: leadership roster -->
  <section class="panel roster">
    <div class="org">
      <h2 class="org-title">The Harrowgate Cardiological Society, Inc.</h2>
      <div class="group">OFFICERS</div>
      <div class="cols">
        <div>
          <p class="officer"><b>Adrian K. Soller</b>, MD, FACC<br>President</p>
          <p class="officer"><b>Graham Pell</b>, MD, FACC<br>Secretary-Treasurer</p>
        </div>
        <div>
          <p class="officer"><b>Edwin Carrow</b>, MD, FACC<br>Immediate Past President</p>
          <p class="officer"><b>Helen Marsden</b>, MA, MSA<br>Executive Director</p>
        </div>
      </div>
      <div class="group">EXECUTIVE BOARD</div>
      <div class="cols">
        <p class="names">Paul Verner, MD, PhD<br>Lydia Crane, MD<br>Owen Hartley, MD, MPH<br>Rupert Flagg, MD<br>Nora Keswick, MD<br>Silas Brede, MD<br>Julian Ferrow, MD</p>
        <p class="names">Adrian K. Soller, MD<br>Carl Denholm, MD<br>Hugh Talbert, Jr., MD<br>Ivan Pratley, MD<br>Ruth Ambrey, MD<br>Dennis Wyatt, MD<br>Omar Halden, MD</p>
      </div>
    </div>

    <div class="org">
      <h2 class="org-title">Halden Cardiac Center</h2>
      <div class="group">OFFICERS</div>
      <div class="cols">
        <div>
          <p class="officer"><b>Leonard P. Astley</b><br>President</p>
          <p class="officer"><b>Victor L. Hensley</b><br>Secretary</p>
        </div>
        <div>
          <p class="officer"><b>Martin E. Rowe</b>, MD<br>Executive Vice President</p>
          <p class="officer"><b>Arthur N. Kellam</b><br>Treasurer</p>
        </div>
      </div>
      <div class="group">BOARD OF GOVERNORS</div>
      <div class="cols">
        <p class="names">Osric Penhallow, DDS<br>Barnaby Quill<br>Victor L. Hensley<br>Hon. Wendell Stroud<br>Ivor Rushmore, Esq.<br>Leonard P. Astley<br>Arthur N. Kellam</p>
        <p class="names">Lionel Fenwick<br>Rufus Calloway, Esq.<br>Silas Marchbank<br>Neville Ostrander, DDS<br>Imogen Halberd, MD<br>Martin E. Rowe, MD<br>Horace Linwood</p>
      </div>
    </div>

    <div class="org">
      <h2 class="org-title">Northvale State Chapter, Allied College of Cardiology</h2>
      <div class="group">OFFICERS</div>
      <div class="cols">
        <div>
          <p class="officer"><b>Edwin Carrow</b>, MD, FACC<br>President</p>
          <p class="officer"><b>Simon Varley</b>, MD, FACC<br>Secretary-Treasurer</p>
        </div>
        <div>
          <p class="officer"><b>Adrian K. Soller</b>, MD, FACC<br>Immediate Past President</p>
          <p class="officer"><b>Helen Marsden</b>, MA, MSA<br>Executive Director</p>
        </div>
      </div>
      <div class="group">COUNCILORS</div>
      <div class="cols">
        <p class="names">Quentin Abernathy, MD, Eastport<br>Felix Ormond, MD, Westvale<br>Casimir Prowse, MD, Harbor City<br>Rowan Eldritch, MD, Bramley<br>Kenji Mabury, MD, Valhurst<br>Beatrix Coulton, MD, Harbor City<br>Hollis Dunstan, MD, Stonebrook<br>Percival Yarde, MD, Marlow</p>
        <p class="names">Tobias Wenlock, MD, Oakridge<br>Ansel Fairbrook, MD, Albury<br>Cyril Hawtrey, MD, Fenwick<br>Lucian Brackett, MD, Oakridge<br>Ellis Trowbridge, MD, Rhineford<br>Gideon Ashcombe, MD, Albury<br>Desmond Verrall, MD, Marlow<br>Ambrose Kettering, MD, Harbor City</p>
      </div>
    </div>
  </section>

  <!-- Panel: mailing side -->
  <section class="panel mailing">
    <div class="seal" aria-hidden="true"></div>
    <div class="return">
      <p class="vline" style="left:8px"><b>The Harrowgate Cardiological Society, Inc.</b><br>220 Merrow Street, Suite 410<br>Harbor City 10240</p>
      <p class="vline" style="left:48px">• <b>88th Annual Scientific Session</b><br>The Harrowgate Cardiological Society, Inc.</p>
      <p class="vline" style="left:86px">• <b>26th Annual Meeting</b><br>Northvale State Chapter<br>Allied College of Cardiology</p>
    </div>
    <div class="map" role="img" aria-label="Map of the island and river around the venue"></div>
  </section>

  <!-- Panel: cover -->
  <section class="panel cover">
    <div class="cover-photo" role="img" aria-label="Photograph of a city skyline with a tall art-deco tower, fading to white"></div>
    <h1 class="cover-title">
      <div class="l1">Cardiology for the</div>
      <div class="l2">Ages: Tailoring Care for</div>
      <div class="l3">OUR AGING POPULATION</div>
    </h1>
    <div class="date-band">
      <div class="row">
        <svg width="14" height="14" viewBox="0 0 14 14" aria-hidden="true"><rect x="1" y="2.5" width="12" height="10.5" rx="1" fill="none" stroke="#fff" stroke-width="1.2"/><line x1="1" y1="5.5" x2="13" y2="5.5" stroke="#fff" stroke-width="1.2"/><line x1="4" y1="1" x2="4" y2="4" stroke="#fff" stroke-width="1.2"/><line x1="10" y1="1" x2="10" y2="4" stroke="#fff" stroke-width="1.2"/><path d="M5 9.3l1.6 1.5 2.8-3" fill="none" stroke="#fff" stroke-width="1.1"/></svg>
        <p class="when">SATURDAY, OCTOBER 8, 2016<br><span>7:30 A.M. – 3:00 P.M.</span></p>
      </div>
      <div class="row">
        <svg width="12" height="14" viewBox="0 0 12 14" style="top:6px" aria-hidden="true"><path d="M6 13s-4.5-4.6-4.5-7.8A4.5 4.5 0 0 1 10.5 5.2C10.5 8.4 6 13 6 13z" fill="#fff"/><circle cx="6" cy="5.3" r="1.7" fill="#1c64a0"/></svg>
        <p class="where"><b>The Corvella Ballroom at Hotel Brisa</b><br>412 Linden Avenue, Harbor City</p>
      </div>
    </div>
    <div class="partners">
      <div class="partner"><i></i><span>In association with<br>Halden Cardiac Center</span></div>
      <div class="partner"><i></i><span>of the Northvale State Chapter,<br>Allied College of Cardiology</span></div>
      <div class="partner"><i></i><span>Presented by<br>The Harrowgate<br>Cardiological Society, Inc.</span></div>
      <div class="partner"><i></i><span>Jointly provided by<br>University of Marlow<br>Center for Applied Learning</span></div>
    </div>
  </section>

  <!-- Panel: program -->
  <section class="panel program">
    <h3 class="h">Program Description</h3>
    <p>As cardiovascular medicine rapidly evolves, clinicians are challenged to choose the best therapies for each patient. This session gives attendees the chance to examine current topics with the goal of helping them provide the best care for their aging patients. The program will include talks from respected specialists from around the country. Lectures will center on acute infarction, imaging for cardiac amyloid, telemonitoring, readmission reduction, atrial fibrillation, aortic stenosis and post-acute care in older adults. Exhibitors will present materials relevant to the advances in therapy being discussed. Regular breaks will allow for networking and give fellows in training the chance to meet clinicians and discuss issues relevant to their future and the current practice of cardiology. In addition, winners of the young investigators research competition will display posters of their work, and two clinical case presentations will be briefly given by the winning fellows and discussed by their mentors.</p>

    <h3 class="h">Target Audience</h3>
    <p>The target audience includes cardiologists, cardiothoracic surgeons, internists, family medicine practitioners, gerontologists, oncologists, cardiac nurse practitioners, physician assistants, cardiology fellows-in-training and all members of the cardiac care team.</p>

    <h3 class="h">Program Objectives</h3>
    <ul>
      <li>At the completion of this program, physicians and other healthcare professionals in attendance will be able to:</li>
      <li>Explain the rationale for, and identify components of, a complete approach to readmission reduction</li>
      <li>Describe the value of high-quality, disease-specific care, planned transitions, team involvement and early outpatient follow-up</li>
      <li>Navigate the current landscape of post-acute care and its relevance to geriatric patients</li>
      <li>Identify gaps in care and specific actions providers can use to improve outcomes</li>
      <li>Identify various types of procedures needed for treating atrial fibrillation in older adults</li>
    </ul>

    <h3 class="h">Program Objectives (cont.)</h3>
    <ul>
      <li>Explain the rationale for why atrial fibrillation care is directed at preventing embolism and controlling rate and rhythm</li>
      <li>Identify the effects of aging on cardiac care and unique aspects of care for older adults</li>
      <li>Delineate the various phenotypes of aortic stenosis in older adults and list the mechanisms of low-flow disease</li>
      <li>Identify cardiac amyloid without a biopsy</li>
      <li>Explain the extent to which current guidelines for cardiac disorders are evidence-based for older adults</li>
      <li>Identify strategies for improving care and outcomes for older adults with heart disease</li>
      <li>Describe the role of non-invasive imaging in the diagnosis of cardiac amyloid</li>
      <li>Recite promising treatments for cardiac amyloidosis</li>
      <li>Describe ways in which telemonitoring can improve heart failure outcomes</li>
      <li>Describe patients' views about the pros and cons of telemonitoring</li>
      <li>Identify management strategies in diagnosing acute MI in elderly patients</li>
    </ul>
  </section>

</main>
</body>
</html>
```